School Auction Party Invitation- Create... the Future.

We need a logo design and invitation for our school auction fundraiser party. Our theme is Create.... The Future. We are trying to incorporate technology, creativity, 21st century learning, and make use of fun, graphic design. colors: black, white, silver, and a bright(almost neon) accent colors. (orange-primary)
Updates

Deadline update: Logo-October 23, Invite- Nov. 7

Target Market(s)

Parents of a private preschool-8th grade students from the Bay Area (majority age 40s, some 30s and 50s) All passionate about kids, education, some varying backgrounds/incomes, but majority upper class-educated. annual school auction/fundraiser. want to create interest/excitement- fun community party. we are trying to focus the theme on creativity & the future (technology, our kid's futures, etc)
www.morvendale.org

Industry/Entity Type

School

Requirements
Must have
• Logo file, One page invite (5x7 including date, time, place, rsvp info, need digital file to print locally

add band logo (possibly tie in to invite look) www.quietharborkitesband.com
Nice to have
• fun, creative, futuristic, abstract, sleek, graphic art. we will be using LED & glow lights at fundraiser
Should not have
• pictures of people

```html
<!DOCTYPE html>
<html lang="en">
<head>
<meta charset="utf-8">
<title>Create... the Future! – Auction Invitation</title>
<link href="https://fonts.googleapis.com/css2?family=Arimo:wght@400;700&family=Silkscreen:wght@700&family=Yellowtail&display=swap" rel="stylesheet">
<style>
  :root {
    --page: #ffffff;
    --card-dark: #1b1b1b;
    --card-mid: #4a4a4a;
    --white: #ffffff;
    --orange: #f7941d;
    --orange-deep: #e8730c;
    --frame: rgba(255,255,255,0.7);
    --grid: rgba(255,255,255,0.12);
  }
  * { box-sizing: border-box; margin: 0; padding: 0; }
  html, body { width: 1200px; height: 836px; overflow: hidden; background: var(--page); }
  body { position: relative; font-family: "Arimo", Arial, sans-serif; color: var(--white); }

  .card {
    position: absolute; top: 33px; width: 539px; height: 757px; overflow: hidden;
    background: radial-gradient(ellipse at 50% 45%, var(--card-mid) 0%, #2c2c2c 55%, var(--card-dark) 100%);
  }
  .card--details { left: 36px; }
  .card--cover { left: 615px; }

  .card__frame { position: absolute; inset: 11px 9px; border: 1px dashed var(--frame); }

  .art-slot { position: absolute; border-radius: 6px; }
  .art-slot--warm { background: linear-gradient(180deg, rgba(247,148,29,.55), rgba(232,80,12,.35)); }
  .art-slot--faint { background: linear-gradient(180deg, rgba(110,76,44,.45), rgba(60,40,24,.35)); }
  .art-slot--cool { background: linear-gradient(180deg, rgba(58,160,224,.5), rgba(90,184,90,.35)); }
  .art-slot--silver { background: linear-gradient(180deg, rgba(200,220,235,.5), rgba(160,140,210,.35)); }

  .brand {
    position: absolute; top: 80px; left: 0; width: 100%; text-align: center;
    font-weight: 700; font-size: 24px; color: var(--orange);
  }

  .headline { position: absolute; left: 0; top: 0; }
  .headline text { font-family: "Silkscreen", "Courier New", monospace; font-weight: 700; }

  .when {
    position: absolute; top: 298px; left: 0; width: 100%;
    display: flex; justify-content: center; align-items: center; gap: 8px;
  }
  .when__date { text-align: right; font-size: 18px; line-height: 1.2; }
  .when__divider { width: 2px; height: 40px; background: var(--orange); }
  .when__time { font-size: 34px; }

  .venue { position: absolute; top: 354px; left: 0; width: 100%; text-align: center; font-size: 14px; }

  .schedule { position: absolute; top: 382px; left: 62px; list-style: none; font-size: 15px; color: var(--orange); }
  .schedule li { display: flex; height: 30px; align-items: center; }
  .schedule__time { width: 96px; }
  .schedule__item::before { content: ""; display: inline-block; width: 5px; height: 5px; border-radius: 50%; background: var(--white); margin: 0 12px 3px 0; vertical-align: middle; }

  .band-note { position: absolute; top: 486px; left: 0; width: 100%; text-align: center; font-size: 13px; line-height: 1.35; }

  .rsvp { position: absolute; top: 543px; left: 0; width: 100%; text-align: center; font-size: 14px; }
  .rsvp-link {
    position: absolute; top: 568px; left: 199px; width: 141px; height: 19px; border-radius: 10px;
    background: var(--orange); color: var(--white); font-size: 13px; text-align: center; line-height: 19px;
  }

  .tagline {
    position: absolute; top: 606px; left: 0; width: 100%; text-align: center;
    font-family: "Yellowtail", cursive; font-size: 15px; color: var(--white);
  }

  .band-mark {
    position: absolute; top: 696px; left: 151px; width: 230px; height: 22px; background: var(--white);
    display: flex; align-items: center; gap: 6px; padding: 0 6px;
    font-size: 15px; color: var(--orange-deep); letter-spacing: .5px;
  }
  .band-mark__square { width: 12px; height: 12px; background: var(--orange-deep); }

  .cover-grid { position: absolute; inset: 0; }
</style>
</head>
<body>

<section class="card card--details">
  <div class="card__frame"></div>

  <div class="art-slot art-slot--faint" style="left:27px;top:47px;width:80px;height:80px" role="img" aria-label="Faint cratered planet illustration"></div>
  <div class="art-slot art-slot--warm" style="left:370px;top:15px;width:160px;height:138px" role="img" aria-label="Orange rocket flying past clouds illustration"></div>

  <div class="brand">Morvendale</div>

  <svg class="headline" width="539" height="300" viewBox="0 0 539 300" role="img" aria-label="Create... the Future!">
    <defs>
      <pattern id="dots-white" width="6" height="6" patternUnits="userSpaceOnUse">
        <circle cx="3" cy="3" r="2.4" fill="#ffffff"/>
      </pattern>
    </defs>
    <text x="104" y="222" font-size="92" textLength="257" lengthAdjust="spacingAndGlyphs" fill="url(#dots-white)">CREATE...</text>
    <text x="53" y="283" font-size="92" textLength="436" lengthAdjust="spacingAndGlyphs" fill="url(#dots-white)">THE FUTURE!</text>
  </svg>

  <div class="when">
    <div class="when__date">Saturday<br>March 22, 2014</div>
    <div class="when__divider"></div>
    <div class="when__time">5:30pm</div>
  </div>

  <p class="venue">Linden Hills Country Club 2400 Alder Crest Drive Linden Hills, CA 94512</p>

  <ul class="schedule">
    <li><span class="schedule__time">5:30 p.m.</span><span class="schedule__item">Silent Auction, Cocktails, and Live Social Time</span></li>
    <li><span class="schedule__time">7:00 p.m.</span><span class="schedule__item">Dinner and Live Auction</span></li>
    <li><span class="schedule__time">8:00 p.m.</span><span class="schedule__item">Live music and dancing</span></li>
  </ul>

  <p class="band-note">Quiet Harbor Kites<br>(Bay area band, and Morvendale parent Dana Whitlow)</p>

  <p class="rsvp">Please return the enclosed rsvp card or rsvp online by March 14</p>
  <div class="rsvp-link">www.morvendale.org</div>

  <div class="art-slot art-slot--faint" style="left:381px;top:588px;width:110px;height:110px;opacity:.7" role="img" aria-label="Faint cratered planet illustration"></div>

  <p class="tagline">Take an exciting trip into the future and celebrate our community!</p>

  <div class="art-slot art-slot--cool" style="left:10px;top:627px;width:85px;height:118px" role="img" aria-label="Desk globe with paper plane illustration"></div>

  <div class="band-mark"><span class="band-mark__square"></span>QUIET HARBOR KITES</div>
</section>

<section class="card card--cover">
  <svg class="cover-grid" width="539" height="757" viewBox="0 0 539 757" aria-hidden="true">
    <g stroke="var(--grid)" stroke-width="2" fill="none">
      <rect x="192" y="206" width="244" height="320"/>
      <line x1="192" y1="206" x2="0" y2="0"/>
      <line x1="436" y1="206" x2="539" y2="0"/>
      <line x1="192" y1="526" x2="0" y2="757"/>
      <line x1="436" y1="526" x2="539" y2="757"/>
      <rect x="150" y="150" width="330" height="430"/>
      <rect x="80" y="70" width="440" height="560"/>
      <line x1="0" y1="560" x2="150" y2="500"/>
      <line x1="539" y1="320" x2="436" y2="350"/>
    </g>
  </svg>

  <div class="art-slot art-slot--cool" style="left:28px;top:52px;width:127px;height:117px" role="img" aria-label="Ringed Earth planet illustration"></div>
  <div class="art-slot art-slot--warm" style="left:200px;top:160px;width:66px;height:66px" role="img" aria-label="Orange cratered planet illustration"></div>
  <div class="art-slot art-slot--warm" style="left:276px;top:15px;width:240px;height:205px" role="img" aria-label="Orange rocket flying past clouds illustration"></div>

  <svg class="headline" width="539" height="540" viewBox="0 0 539 540" role="img" aria-label="Create... the Future!">
    <defs>
      <pattern id="dots-orange" width="8" height="8" patternUnits="userSpaceOnUse">
        <circle cx="4" cy="4" r="3.3" fill="#f7941d"/>
      </pattern>
    </defs>
    <text x="59" y="333" font-size="110" textLength="430" lengthAdjust="spacingAndGlyphs" fill="url(#dots-orange)">CREATE...</text>
    <text x="194" y="418" font-size="110" textLength="166" lengthAdjust="spacingAndGlyphs" fill="url(#dots-orange)">THE</text>
    <text x="60" y="505" font-size="110" textLength="400" lengthAdjust="spacingAndGlyphs" fill="url(#dots-orange)">FUTURE!</text>
  </svg>

  <div class="art-slot art-slot--silver" style="left:25px;top:610px;width:132px;height:106px" role="img" aria-label="Cartoon flying saucer illustration"></div>
  <div class="art-slot art-slot--cool" style="left:389px;top:546px;width:111px;height:133px" role="img" aria-label="Telescope on tripod illustration"></div>
</section>

</body>
</html>
```